Innovative Consulting Firm Needs New Business Cards and Stationary

Our Innovative Consulting Firm, Larkfield Consulting, is in need of new business cards and stationary designs. We want two-sided cards that incorporate our logo, which is attached. We are looking for something not too formal, but is professional and slick.

Card should have the following information:
Name (ex. Tom Bradley)
Title (ex. Manager)
Address (ex. 24680 Cedar Lane)
Address 2 (ex. Suite 100)
City
State
Zip Code
Mobile
Email

The card should also have our website: www.larkfieldconsulting.example

Industry/Entity Type

Management Consulting

Contact Information for Business Card

Name (ex. Tom Bradley)
Title (ex. Manager)
Address 2 (ex. Suite 100)
City
State
Zip Code
Mobile
Email

Font styles to use
Sans Serif

Requirements
Must have
• The colors on the card must match the colors in the logo. The exact color codes are attached in a pdf.
Nice to have
• The Company's Tagline is "Focused on your Future". This might be nice to incorporate, but not necessary.

```html
<!DOCTYPE html>
<html lang="en">
<head>
<meta charset="utf-8">
<title>Larkfield Consulting – Business Card</title>
<link rel="stylesheet" href="https://fonts.googleapis.com/css2?family=Open+Sans:wght@400;600;700&display=swap">
<style>
  :root {
    --navy: #25507f;
    --gold: #f3b21b;
    --card: #eef3f9;
    --ink: #2f2f33;
    --stage: #dfe2e6;
  }
  * { box-sizing: border-box; margin: 0; padding: 0; }
  html, body {
    width: 1200px; height: 882px; overflow: hidden;
    background: var(--stage);
    font-family: "Open Sans", Arial, sans-serif;
  }
  .card {
    position: absolute;
    width: 620px; height: 354px;
    left: 290px;
    background: var(--card);
    overflow: hidden;
    box-shadow: 0 6px 18px rgba(0,0,0,.18);
  }
  .card--front { top: 70px; }
  .card--back { top: 458px; }
  .card-shapes { position: absolute; inset: 0; }

  .brand { position: absolute; display: flex; align-items: center; gap: 10px; }
  .brand-dot { width: 16px; height: 16px; border-radius: 50%; background: var(--gold); }
  .brand-name { color: var(--navy); font-weight: 600; font-size: 30px; line-height: 1; letter-spacing: .2px; }

  .card--front .brand { left: 112px; top: 118px; }
  .tagline {
    position: absolute; left: 200px; top: 180px;
    color: var(--navy); font-size: 18px;
  }

  .card--back .brand { left: 30px; top: 70px; }
  .card--back .brand-name { font-size: 25px; }
  .person { position: absolute; right: 110px; top: 56px; text-align: left; }
  .person-name { color: var(--navy); font-size: 26px; font-weight: 700; letter-spacing: .5px; }
  .person-title { color: var(--gold); font-size: 14px; font-weight: 600; letter-spacing: 1px; margin-top: 2px; }
  .contacts {
    position: absolute; right: 90px; top: 150px;
    text-align: right; color: var(--ink); font-size: 15px; line-height: 22px;
    list-style: none;
  }
  .contact-icons {
    position: absolute; right: 26px; top: 154px;
    display: flex; flex-direction: column; gap: 6px;
  }
  .contact-icons svg { width: 16px; height: 16px; display: block; }
  .address {
    position: absolute; left: 34px; bottom: 26px;
    color: var(--gold); font-size: 17px; line-height: 24px;
  }
</style>
</head>
<body>

<section class="card card--front" aria-label="Card front">
  <svg class="card-shapes" viewBox="0 0 620 354" aria-hidden="true">
    <polygon points="250,354 620,196 620,234 338,354" fill="var(--gold)"/>
  </svg>
  <div class="brand">
    <span class="brand-dot"></span>
    <span class="brand-name">Larkfield Consulting</span>
  </div>
  <p class="tagline">Focused on your Future</p>
</section>

<section class="card card--back" aria-label="Card back">
  <svg class="card-shapes" viewBox="0 0 620 354" aria-hidden="true">
    <rect x="552" y="0" width="68" height="272" fill="var(--navy)"/>
    <polygon points="330,282 620,272 620,290 338,300" fill="var(--gold)"/>
    <polygon points="0,266 316,266 350,354 0,354" fill="var(--navy)"/>
  </svg>

  <div class="brand">
    <span class="brand-dot"></span>
    <span class="brand-name">Larkfield Consulting</span>
  </div>

  <div class="person">
    <p class="person-name">TOM BRADLEY</p>
    <p class="person-title">MANAGER</p>
  </div>

  <ul class="contacts">
    <li>+47 555 010 42</li>
    <li>www.larkfieldconsulting.example</li>
    <li>info@larkfieldconsulting.example</li>
  </ul>

  <div class="contact-icons" aria-hidden="true">
    <svg viewBox="0 0 16 16"><path d="M4 2l3 3-2 2c1 2 2 3 4 4l2-2 3 3-2 2C7 14 2 9 2 4z" fill="var(--gold)"/></svg>
    <svg viewBox="0 0 16 16"><circle cx="8" cy="8" r="6" fill="none" stroke="var(--gold)" stroke-width="1.6"/><path d="M2 8h12M8 2c-3 3-3 9 0 12M8 2c3 3 3 9 0 12" fill="none" stroke="var(--gold)" stroke-width="1.2"/></svg>
    <svg viewBox="0 0 16 16"><rect x="1.5" y="3.5" width="13" height="9" fill="var(--gold)"/><path d="M1.5 3.5l6.5 5 6.5-5" fill="none" stroke="var(--navy)" stroke-width="1.2"/></svg>
  </div>

  <p class="address">24680 Cedar Lane<br>ex. Suite 100</p>
</section>

</body>
</html>
```